Business Card Design Project

We need a logo design for a new company based in Southern California called "Brocklin Security Services, Inc." We install security and camera systems for homeowners and business, to protect their assets.
Updates

Project Deadline Extended
Reason: LOGO Design completes in eight days. Would like that design decided before we finish the business cards. Thanks...

Target Market(s)

Homeowners and business owners looking for additional protection of their assets.

Industry/Entity Type

Security

Font styles to use
Serif

Requirements
Must have
• Company Name
Office# 555-204-6137
Service# 555-204-6138
email: BrocklinSecurity@quorvex.net
address: 48210 Maple Row Harlow Springs, NV 90000
Nice to have
• Serving the Harlow Valley

```html
<!DOCTYPE html>
<html lang="en">
<head>
<meta charset="utf-8">
<title>Brocklin Security Services – Business Card</title>
<link rel="stylesheet" href="https://fonts.googleapis.com/css2?family=Open+Sans:wght@400;600;700&display=swap">
<style>
  :root {
    --bg: #e9e6e1;
    --card-white: #fbfbfb;
    --card-white-edge: #eaeaea;
    --brand-red: #e0212f;
    --brand-red-dark: #c81a27;
    --band-grey: #a9a9ab;
    --line-grey: #c9c9cb;
    --text-grey: #8a8a8c;
    --text-white: #ffffff;
  }
  * { margin: 0; padding: 0; box-sizing: border-box; }
  html, body {
    width: 1200px; height: 1023px; overflow: hidden;
    background: var(--bg);
    font-family: "Open Sans", Arial, sans-serif;
  }
  .stage {
    width: 1200px; height: 1023px;
    display: flex; align-items: center; justify-content: center;
  }
  .card {
    position: relative;
    width: 1000px; height: 572px;
    background: linear-gradient(180deg, var(--card-white) 0%, var(--card-white-edge) 100%);
    overflow: hidden;
    box-shadow: 0 10px 30px rgba(0,0,0,.18);
  }
  .brand {
    position: absolute; left: 70px; top: 110px;
    display: flex; align-items: center; gap: 22px;
  }
  .brand-mark {
    width: 26px; height: 26px; border-radius: 50%;
    background: var(--brand-red);
  }
  .brand-name {
    font-size: 44px; font-weight: 600;
    font-variant: small-caps; letter-spacing: 1px;
    color: var(--text-grey); line-height: 1.05;
  }
  .red-band {
    position: absolute; left: 0; top: 300px;
    width: 100%; height: 180px;
    background: linear-gradient(180deg, var(--brand-red) 0%, var(--brand-red-dark) 100%);
  }
  .grey-band {
    position: absolute; left: 0; top: 480px;
    width: 100%; height: 92px;
    background: var(--band-grey);
  }
  .band-rules { position: absolute; left: 0; top: 300px; width: 1000px; height: 200px; }
  .holder { position: absolute; left: 70px; top: 330px; color: var(--text-white); }
  .holder-name { font-size: 30px; font-weight: 700; }
  .holder-role { font-size: 24px; font-weight: 400; }
  .holder-role::before { content: "|"; margin: 0 10px 0 8px; opacity: .8; }
  .contact-list { list-style: none; margin-top: 12px; }
  .contact-list li {
    display: flex; align-items: center; gap: 12px;
    font-size: 20px; line-height: 30px;
  }
  .contact-icon { width: 18px; height: 18px; flex: none; }
  .address {
    position: absolute; left: 600px; top: 350px;
    display: flex; align-items: flex-start; gap: 16px;
    color: var(--text-white); font-size: 22px; line-height: 30px;
    font-style: normal;
  }
  .address-icon { width: 40px; height: 40px; flex: none; margin-top: 12px; }
  .tagline {
    position: absolute; left: 210px; top: 510px;
    color: var(--text-white); font-size: 22px; letter-spacing: .5px;
  }
</style>
</head>
<body>
<main class="stage">
  <article class="card">
    <header class="brand">
      <span class="brand-mark"></span>
      <span class="brand-name">Brocklin Security<br>Services, Inc.</span>
    </header>

    <div class="red-band"></div>
    <div class="grey-band"></div>

    <svg class="band-rules" viewBox="0 0 1000 200" aria-hidden="true">
      <line x1="0" y1="22" x2="1000" y2="22" stroke="var(--line-grey)" stroke-width="3"/>
      <polygon points="560,22 584,22 572,38" fill="var(--line-grey)"/>
      <polygon points="560,180 584,180 572,196" fill="var(--brand-red-dark)"/>
    </svg>

    <section class="holder">
      <p><span class="holder-name">Dale Whitmore</span><span class="holder-role">Director</span></p>
      <ul class="contact-list">
        <li>
          <svg class="contact-icon" viewBox="0 0 20 20"><circle cx="10" cy="10" r="9" fill="none" stroke="#fff" stroke-width="1.5"/><path d="M7 5.5c-1 1-1 3 1.5 5.5s4.5 2.5 5.5 1.5l-1.6-1.6-1.3.7c-1-.5-2.2-1.7-2.7-2.7l.7-1.3z" fill="#fff"/></svg>
          555-204-6137 [Office]
        </li>
        <li>
          <svg class="contact-icon" viewBox="0 0 20 20"><circle cx="10" cy="10" r="9" fill="none" stroke="#fff" stroke-width="1.5"/><path d="M7 5.5c-1 1-1 3 1.5 5.5s4.5 2.5 5.5 1.5l-1.6-1.6-1.3.7c-1-.5-2.2-1.7-2.7-2.7l.7-1.3z" fill="#fff"/></svg>
          555-204-6138 [Service]
        </li>
        <li>
          <svg class="contact-icon" viewBox="0 0 20 20"><circle cx="10" cy="10" r="9" fill="none" stroke="#fff" stroke-width="1.5"/><rect x="5" y="6.5" width="10" height="7" fill="none" stroke="#fff" stroke-width="1.3"/><path d="M5 6.5l5 4 5-4" fill="none" stroke="#fff" stroke-width="1.3"/></svg>
          BrocklinSecurity@quorvex.net
        </li>
      </ul>
    </section>

    <address class="address">
      <svg class="address-icon" viewBox="0 0 40 40"><circle cx="20" cy="20" r="18" fill="none" stroke="#fff" stroke-width="2"/><path d="M20 9a7 7 0 0 0-7 7c0 5 7 14 7 14s7-9 7-14a7 7 0 0 0-7-7z" fill="#fff"/><circle cx="20" cy="16" r="2.6" fill="var(--brand-red)"/></svg>
      <span>48210 Maple Row Harlow<br>Springs,<br>NV 90000</span>
    </address>

    <p class="tagline">Serving the Harlow Valley</p>
  </article>
</main>
</body>
</html>
```